"Parker's True Grain Woodwork" with a logo of a saw blade and handplane combined

Need a business card logo with a saw blade and hand plane
combined with Parker's True Grain Woodwork on it, and a unique design.

Woodworking has been in my family for generations, from carpentry, to milling logs for old farm homes and barns in the 1930's and 1940's. My grandfather had a small carpentry business from his home,and passed his skills down to my father who also did woodworking from his own small business. Having the passion for woodwork in my blood, I'm trying to continue with my own small business doing custom fine woodwork such as tables, small cabinetry and even outdoor projects to suite the customers needs. All my projects start with a rough piece of lumber, what ever the species suited for the project, and is milled to dimensions , assembled, and finished all by hand for a true handcrafted project.

My target market would be people who want a custom handmade piece, something that they can't find in stores and is unique. Also people who are willing to pay and appreciate the value, which is sometimes a hard market to find.

As far as design, I think I would like to get a sleek looking saw blade on the card combined with a hand plane some how. Background colour maybe a dark wood texture or grey? Colours I like are grey, black, reds, white, yellows but depending on how the card is looking I'm not afraid to use a cool colour to make something stand out. Just want the card to flow ,look clean and unique. Lettering I like serif and script or something similar to these that looks good on the card.

Facebook page is under Parker's True Grain Woodwork
Updates

If I could get logo on the card, a saw blade, hand plane or combine both together would be nice! Added Saturday, June 11, 2016

Target Market(s)

People that like a unique hand made project built to last

Industry/Entity Type

Business

Contact Information for Business Card

Parkers True Grain Woodwork
Hand crafted by: Owen Parker
Phone: 905 618-2297
Address: 412 Birchview Rd. Alderbrook-On-The-Bay
Email: parkerstruegrain@mailbox-example.com
Facebook: Parkers True Grain Woodwork
prefer icons for the info!

Font styles to use
Serif
Script

Requirements
Must have
• Nice clean look, little bit bold with an elegant taste
• Prefer black lettering
Nice to have
• I like silver for the saw blade and silver with brown handles on the hand plane!
Should not have
• Bright colours

```html
<!DOCTYPE html>
<html lang="en">
<head>
<meta charset="utf-8">
<title>Parker's True Grain Woodwork – Business Card</title>
<link rel="stylesheet" href="https://fonts.googleapis.com/css2?family=Open+Sans:wght@400;600&family=Noto+Serif:wght@400&display=swap">
<style>
  :root {
    --canvas: #ecebe8;
    --brown: #472a25;
    --brown-text: #4a2c26;
    --paper: #ffffff;
    --paper-shade: #ececec;
    --ink: #111111;
    --on-brown: #ffffff;
    --mark-square: #d9c7b0;
    --shadow: rgba(40, 25, 20, 0.28);
  }
  html, body {
    margin: 0;
    padding: 0;
    width: 1200px;
    height: 900px;
    overflow: hidden;
    background: var(--canvas);
    font-family: "Open Sans", Arial, sans-serif;
  }
  .canvas {
    position: relative;
    width: 1200px;
    height: 900px;
  }
  .card {
    position: absolute;
    width: 560px;
    height: 320px;
    box-shadow: 0 10px 24px var(--shadow);
    overflow: hidden;
  }

  /* Front of card */
  .card-front {
    left: 60px;
    top: 110px;
    background: var(--brown);
  }
  .card-front .brand {
    position: absolute;
    left: 150px;
    top: 98px;
    display: flex;
    align-items: center;
    gap: 20px;
    color: var(--on-brown);
  }
  .brand-dot {
    width: 74px;
    height: 74px;
    border-radius: 50%;
    background: var(--on-brown);
    flex: none;
  }
  .brand-name {
    line-height: 1;
  }
  .brand-name .primary {
    display: block;
    font-weight: 400;
    font-size: 40px;
    letter-spacing: 0.5px;
  }
  .brand-name .secondary {
    display: block;
    font-family: "Noto Serif", Georgia, serif;
    font-size: 15px;
    margin-top: 4px;
    padding-left: 16px;
  }
  .social-square {
    position: absolute;
    left: 268px;
    top: 222px;
    width: 24px;
    height: 24px;
    border-radius: 3px;
    background: var(--mark-square);
  }

  /* Back of card */
  .card-back {
    left: 580px;
    top: 470px;
    background: var(--brown);
  }
  .card-back .top-band {
    position: absolute;
    left: 0;
    top: 0;
    width: 100%;
    height: 150px;
    background: linear-gradient(180deg, var(--paper-shade) 0%, var(--paper) 40%, var(--paper) 100%);
  }
  .card-back .divider {
    position: absolute;
    left: 0;
    top: 150px;
    width: 100%;
    height: 4px;
    background: var(--ink);
  }
  .card-back .divider-gap {
    position: absolute;
    left: 0;
    top: 154px;
    width: 100%;
    height: 10px;
    background: var(--paper);
  }
  .card-back .brand {
    position: absolute;
    left: 150px;
    top: 34px;
    display: flex;
    align-items: center;
    gap: 20px;
    color: var(--brown-text);
  }
  .card-back .brand-dot {
    background: var(--ink);
  }
  .contact-lines {
    position: absolute;
    right: 240px;
    top: 200px;
    text-align: right;
    color: var(--on-brown);
    font-size: 14px;
    line-height: 1;
  }
  .contact-lines .row {
    display: flex;
    justify-content: flex-end;
    align-items: center;
    gap: 8px;
    margin-bottom: 12px;
  }
  .contact-lines svg {
    width: 12px;
    height: 12px;
    flex: none;
  }
  .person {
    position: absolute;
    left: 342px;
    top: 176px;
    color: var(--on-brown);
  }
  .person .name {
    font-weight: 600;
    font-size: 16px;
    margin: 0 0 8px;
  }
  .person .address {
    font-size: 12px;
    line-height: 1.6;
    font-style: normal;
    padding-left: 14px;
  }
</style>
</head>
<body>
<main class="canvas">

  <section class="card card-front" aria-label="Card front">
    <div class="brand">
      <span class="brand-dot"></span>
      <span class="brand-name">
        <span class="primary">PARKER'S</span>
        <span class="secondary">True Grain Woodwork</span>
      </span>
    </div>
    <span class="social-square" aria-hidden="true"></span>
  </section>

  <section class="card card-back" aria-label="Card back">
    <div class="top-band"></div>
    <div class="divider"></div>
    <div class="divider-gap"></div>

    <div class="brand">
      <span class="brand-dot"></span>
      <span class="brand-name">
        <span class="primary">PARKER'S</span>
        <span class="secondary">True Grain Woodwork</span>
      </span>
    </div>

    <div class="contact-lines">
      <div class="row phone">
        <span>555 618-2297</span>
        <svg viewBox="0 0 24 24" aria-hidden="true"><path fill="#fff" d="M6.6 10.8a15.1 15.1 0 0 0 6.6 6.6l2.2-2.2c.3-.3.7-.4 1-.2 1.1.4 2.3.6 3.6.6.6 0 1 .4 1 1V20c0 .6-.4 1-1 1C10.6 21 3 13.4 3 4c0-.6.4-1 1-1h3.5c.6 0 1 .4 1 1 0 1.3.2 2.5.6 3.6.1.3 0 .7-.2 1z"/></svg>
      </div>
      <div class="row email">
        <span>parkerstruegrain@mailbox-example.com</span>
        <svg viewBox="0 0 24 24" aria-hidden="true"><rect x="2" y="5" width="20" height="14" rx="1" fill="#fff"/><path d="M2.5 5.5 12 13l9.5-7.5" fill="none" stroke="#472a25" stroke-width="1.8"/></svg>
      </div>
    </div>

    <div class="person">
      <p class="name">Owen Parker</p>
      <address class="address">412 Birchview Rd.<br>Alderbrook-On-The-Bay</address>
    </div>
  </section>

</main>
</body>
</html>
```